Design some Business Cards for my business running bachelorette parties

Hi, I am starting a business on the central coast running bachelorette parties and need some kick ass business cards - you know ones that make people sit up and go Wow!! I am also putting together a website for my business as well - so if your design is really kick ass we can discuss how much you would charge to let me use it on my website - or possibly to do my website. :)

I am looking for classy, fun, off beat, unique - something with some personality - like me :) Please feel free to email me questions and bounce ideas off me. And have fun!!!!

```html
<!DOCTYPE html>
<html lang="en">
<head>
<meta charset="utf-8">
<title>Bachelorette Parties – Business Card</title>
<link rel="stylesheet" href="https://fonts.googleapis.com/css2?family=Lobster+Two:ital,wght@1,700&family=Gelasio:ital,wght@1,700&family=Arimo&display=swap">
<style>
  :root {
    --backdrop: #ece8e6;
    --stripe-light: #f6d9e3;
    --stripe-dark: #eec5d3;
    --band-grey: #bdbdbd;
    --band-base: #f2f2f2;
    --rule-dark: #2b1b22;
    --rule-accent: #b8346a;
    --brand: #b8346a;
    --ink: #3a2a31;
    --muted: #4a4a4a;
    --shoe-dark: #141414;
    --shoe-mid: #2e2e2e;
  }
  * { box-sizing: border-box; margin: 0; padding: 0; }
  html, body { width: 1200px; height: 749px; overflow: hidden; }
  body { background: var(--backdrop); position: relative; }

  .card {
    position: absolute;
    width: 474px;
    height: 274px;
    background: repeating-linear-gradient(90deg,
      var(--stripe-light) 0 13px, var(--stripe-dark) 13px 26px);
    box-shadow: 0 4px 14px rgba(0,0,0,.18);
    overflow: hidden;
  }
  .card--front { left: 143px; top: 97px; }
  .card--back  { left: 633px; top: 408px; }

  .pattern-band {
    position: absolute; left: 0; width: 100%; height: 41px;
    background: linear-gradient(180deg, var(--band-base), var(--band-grey) 50%, var(--band-base));
  }
  .pattern-band--top { top: 0; }
  .pattern-band--bottom { bottom: 0; height: 40px; }

  .rule {
    position: absolute; left: 0; width: 100%; height: 6px;
    border-top: 4px solid var(--rule-dark);
    border-bottom: 2px solid var(--rule-accent);
  }
  .rule--top { top: 41px; }
  .rule--bottom { bottom: 40px; }

  .shoe-art {
    position: absolute; left: 16px; top: 68px; width: 100px; height: 152px;
    background: radial-gradient(ellipse at 50% 60%, var(--shoe-mid), var(--shoe-dark) 70%);
    border-radius: 18px;
  }

  .title {
    position: absolute; font-family: "Lobster Two", cursive;
    font-style: italic; font-weight: 700; color: var(--brand);
    font-size: 44px; line-height: 1; white-space: nowrap;
  }
  .title--line1 { left: 128px; top: 68px; }
  .title--line2 { right: 64px; top: 110px; }

  .tagline {
    position: absolute; left: 262px; top: 176px;
    font-family: "Arimo", sans-serif; font-size: 16px; color: var(--muted);
    white-space: nowrap;
  }

  .contact {
    position: absolute; left: 124px; top: 58px; list-style: none;
  }
  .contact li {
    display: flex; align-items: center; height: 36px;
    font-family: "Gelasio", serif; font-style: italic; font-weight: 700;
    font-size: 17px; color: var(--ink); white-space: nowrap;
  }
  .contact .icon {
    width: 20px; height: 20px; margin-right: 13px; fill: var(--brand);
    font-family: "Arimo", sans-serif; font-weight: 700; font-style: normal;
    color: var(--brand); font-size: 21px; line-height: 20px; text-align: center;
  }
  .website {
    position: absolute; left: 0; width: 100%; top: 194px; text-align: center;
    font-family: "Gelasio", serif; font-weight: 700; font-size: 19px; color: var(--ink);
    padding-left: 24px;
  }
</style>
</head>
<body>
  <section class="card card--front">
    <div class="pattern-band pattern-band--top" role="img" aria-label="Grey damask ornamental pattern"></div>
    <div class="rule rule--top"></div>
    <div class="shoe-art" role="img" aria-label="Illustration of a pair of black high-heel stilettos with red soles"></div>
    <div class="title title--line1">Bachelorette</div>
    <div class="title title--line2">parties</div>
    <p class="tagline">for a night to remember</p>
    <div class="rule rule--bottom"></div>
    <div class="pattern-band pattern-band--bottom" role="img" aria-label="Grey damask ornamental pattern"></div>
  </section>

  <section class="card card--back">
    <div class="pattern-band pattern-band--top" role="img" aria-label="Grey damask ornamental pattern"></div>
    <div class="rule rule--top"></div>
    <ul class="contact">
      <li><span class="icon">@</span>hello@velvetnights.com</li>
      <li>
        <svg class="icon" viewBox="0 0 24 24" aria-hidden="true"><path d="M6.6 10.8a15.1 15.1 0 0 0 6.6 6.6l2.2-2.2c.3-.3.7-.4 1-.2 1.1.4 2.3.6 3.6.6.6 0 1 .4 1 1V20c0 .6-.4 1-1 1A17 17 0 0 1 3 4c0-.6.4-1 1-1h3.5c.6 0 1 .4 1 1 0 1.3.2 2.5.6 3.6.1.3 0 .7-.2 1z"/></svg>
        555 018 2734
      </li>
      <li>
        <svg class="icon" viewBox="0 0 24 24" aria-hidden="true"><path d="M12 3 2 12h3v9h5v-6h4v6h5v-9h3z"/></svg>
        48 Harbour Lane, NY
      </li>
    </ul>
    <p class="website">www.velvetnights.com</p>
    <div class="rule rule--bottom"></div>
    <div class="pattern-band pattern-band--bottom" role="img" aria-label="Grey damask ornamental pattern"></div>
  </section>
</body>
</html>
```